Need Web Design for Business Process Outsourcing Company (Korvenza)

Korvenza is a business process outsourcing company. Need a simple site similar to http://www.taskmeridianhub.com/ but with a more professional and credible look. New to the process; not sure where to start and comparing my options. Please let me know what my options are if I choose to go with you. Logo is attached for your reference. Please use same colorway

Reason: I want the final product to be coded. Please confirm you will be able to code final design.

Industry/Entity Type

Business

Coding

Coded - Design and coding required

```html
<!DOCTYPE html>
<html lang="en">
<head>
<meta charset="utf-8">
<title>Korvenza — Business Process Outsourcing</title>
<link href="https://fonts.googleapis.com/css2?family=Oswald:wght@300;400;600&family=Open+Sans:wght@300;400;600;700&family=Lato:wght@400;700&display=swap" rel="stylesheet">
<style>
:root{
  --brand:#1b87c9;
  --brand-dark:#0b5692;
  --navy:#0d4f86;
  --ink:#333b44;
  --muted:#7b8590;
  --line:#e4e8ec;
  --white:#ffffff;
  --footer:#1d8fd0;
}
*{box-sizing:border-box;margin:0;padding:0}
html,body{width:1200px;height:3041px;overflow:hidden;background:var(--white)}
body{font-family:'Lato',sans-serif;color:var(--ink)}
.page{position:relative;width:1200px;height:3041px;overflow:hidden}
.abs{position:absolute}

/* header */
.brand{left:100px;top:36px;display:flex;align-items:center;gap:12px}
.brand-mark{width:40px;height:40px;background:var(--brand-dark);border-radius:4px}
.brand-name{font-family:'Open Sans',sans-serif;font-weight:700;font-size:34px;color:var(--brand-dark);letter-spacing:-.5px}
.phone{left:735px;top:44px;display:flex;align-items:center;gap:12px;font-family:'Open Sans',sans-serif}
.phone-icon{width:42px;height:42px;border-radius:50%;background:var(--brand);display:flex;align-items:center;justify-content:center}
.phone-label{font-size:11px;color:var(--muted);letter-spacing:.5px}
.phone-num{font-size:20px;font-weight:700;color:var(--brand-dark)}
.chat-btn{left:993px;top:48px;width:108px;height:38px;border:1.5px solid var(--brand);border-radius:3px;color:var(--brand);font:700 11px 'Open Sans',sans-serif;display:flex;align-items:center;justify-content:center;gap:6px;letter-spacing:.4px}

.nav{left:0;top:132px;width:1200px;height:54px;background:var(--brand-dark);display:flex;padding-left:100px}
.nav a{color:var(--white);text-decoration:none;font:400 11px 'Open Sans',sans-serif;letter-spacing:.3px;height:54px;display:flex;align-items:center;justify-content:center}
.nav a.active{background:var(--brand)}

/* hero */
.hero-photo{left:95px;top:230px;width:620px;height:430px;background:linear-gradient(135deg,#e9eef2 0%,#cfd7de 55%,#8c959e 100%);border-radius:2px}
.hero-swoosh{left:0;top:470px}
.hero-sub{left:786px;top:272px;font:300 32px 'Oswald',sans-serif;color:var(--navy);letter-spacing:.5px}
.hero-title{left:784px;top:310px;font:600 58px 'Oswald',sans-serif;color:var(--navy);letter-spacing:1px}
.hero-text{left:786px;top:396px;width:330px;font:400 13.5px/22px 'Open Sans',sans-serif;color:#4e5863}
.btn-outline{border:1.5px solid var(--brand);border-radius:3px;color:var(--brand-dark);font:700 10.5px 'Open Sans',sans-serif;display:flex;align-items:center;justify-content:center;gap:7px;letter-spacing:.3px;background:var(--white)}
.hero-btn{left:786px;top:473px;width:145px;height:39px}
.hero-arrow{top:318px}

/* section heading */
.sec-title{left:0;width:1200px;text-align:center;font:300 28px 'Open Sans',sans-serif;letter-spacing:.5px;color:#2b2f35}
.sec-title b{font-weight:700}

/* services */
.service{width:264px;text-align:center}
.service-icon{width:88px;height:88px;border:2px solid var(--navy);border-radius:50%;margin:0 auto;display:flex;align-items:center;justify-content:center}
.service h3{margin-top:22px;font:700 14px 'Open Sans',sans-serif;color:var(--navy)}
.service p{margin-top:10px;font:400 11.5px/21px 'Open Sans',sans-serif;color:var(--muted)}

/* strategy */
.strategy{left:0;top:1083px;width:1200px;height:490px;background:linear-gradient(100deg,#2d96d6 0%,#1f86c8 45%,#1776b8 75%,#1c7fbf 100%)}
.strategy .sec-title{color:var(--white)}
.strat-item{width:470px;display:flex;gap:32px;color:var(--white)}
.strat-item h4{font:400 14px 'Open Sans',sans-serif}
.strat-item .rule{width:42px;height:2px;background:var(--white);margin:12px 0 14px}
.strat-item p{font:400 11.5px/21px 'Open Sans',sans-serif;opacity:.92}

/* news */
.news-img{border-radius:4px}
.news-title{font:700 14px 'Open Sans',sans-serif;color:var(--navy)}
.news-text{width:645px;font:400 11.5px/22px 'Open Sans',sans-serif;color:var(--muted)}
.news-btn{width:178px;height:40px}

.divider{left:100px;top:2240px;width:1000px;height:1px;background:var(--line)}
.quote{left:0;top:2300px;width:1200px;text-align:center;font:400 21px/33px 'Open Sans',sans-serif;color:var(--brand)}
.quote-text{left:125px;top:2380px;width:950px;text-align:center;font:400 11.5px/22px 'Open Sans',sans-serif;color:var(--muted)}
.join-btn{left:542px;top:2470px;width:116px;height:40px}

/* footer */
.footer{left:0;top:2600px;width:1200px;height:325px;background:linear-gradient(110deg,#1676b8 0%,#1e8dd0 50%,#2aa0e0 100%)}
.foot-h{font:700 15px 'Open Sans',sans-serif;color:var(--white);letter-spacing:.3px}
.foot-p{font:400 11.5px/22px 'Open Sans',sans-serif;color:#e3f1fb}
.contact-row{display:flex;gap:14px;align-items:flex-start}
.social{display:flex;gap:8px}
.social span{width:26px;height:26px;border-radius:50%;background:var(--white)}
.field{width:291px;height:34px;border:1px solid #cfe7f6;color:var(--white);font:400 11px 'Open Sans',sans-serif;padding:0 14px;display:flex;align-items:center}
.field-btn{justify-content:center;font-weight:700;font-size:11px;letter-spacing:.3px}

.bottom-links{left:0;top:2958px;width:1200px;text-align:center;font:400 10.5px 'Open Sans',sans-serif;color:#4f5963}
.bottom-links span{margin:0 8px;color:#9aa3ab}
.copyright{left:0;top:2996px;width:1200px;text-align:center;font:400 10px 'Open Sans',sans-serif;color:#6b747d}
</style>
</head>
<body>
<div class="page">

  <!-- Header -->
  <div class="abs brand"><span class="brand-mark"></span><span class="brand-name">Korvenza</span></div>
  <div class="abs phone">
    <span class="phone-icon"><svg width="20" height="20" viewBox="0 0 24 24" fill="none" stroke="#fff" stroke-width="1.8"><path d="M5 3h4l2 5-2.5 1.5a11 11 0 0 0 6 6L16 13l5 2v4a2 2 0 0 1-2 2A16 16 0 0 1 3 5a2 2 0 0 1 2-2z"/></svg></span>
    <span class="phone-label">PHONE :</span><span class="phone-num">(555) 214-3690</span>
  </div>
  <div class="abs chat-btn">LIVE CHAT <svg width="13" height="12" viewBox="0 0 24 22" fill="none" stroke="#1b87c9" stroke-width="2"><path d="M3 3h18v12H9l-5 4v-4H3z"/></svg></div>

  <nav class="abs nav">
    <a class="active" style="width:137px">HOME</a>
    <a style="width:137px">WHO WE ARE</a>
    <a style="width:124px">OUR SERVICES</a>
    <a style="width:144px">OUR STRATEGY</a>
    <a style="width:107px">SECURITY</a>
    <a style="width:88px">NEWS</a>
    <a style="width:127px">CONTACT US</a>
  </nav>

  <!-- Hero -->
  <div class="abs hero-photo" role="img" aria-label="Smiling customer support agent with headset working at a desktop computer"></div>
  <svg class="abs hero-swoosh" width="1200" height="200" viewBox="0 0 1200 200">
    <path d="M0 22 C 180 95, 380 175, 660 182 C 880 186, 1060 110, 1200 40 L1200 60 C 1060 130, 880 200, 660 200 L0 200 Z" fill="#fff"/>
    <path d="M0 22 C 180 95, 380 175, 660 182 C 880 186, 1060 110, 1200 40 C 1060 120, 880 172, 660 170 C 400 166, 200 110, 0 48 Z" fill="#1b87c9"/>
  </svg>
  <svg class="abs hero-arrow" style="left:36px" width="20" height="52" viewBox="0 0 20 52"><path d="M18 2 L3 26 L18 50" fill="none" stroke="#cfd6dc" stroke-width="2"/></svg>
  <svg class="abs hero-arrow" style="left:1144px" width="20" height="52" viewBox="0 0 20 52"><path d="M2 2 L17 26 L2 50" fill="none" stroke="#cfd6dc" stroke-width="2"/></svg>

  <div class="abs hero-sub">BUSINESS PROCESS</div>
  <div class="abs hero-title">OUTSOURCING</div>
  <p class="abs hero-text">Aspernatur aut odit aut fugit, sed quia consequuntur magni dolores eos qui ratione voluptatem...</p>
  <div class="abs btn-outline hero-btn"><svg width="12" height="12" viewBox="0 0 24 24" fill="#1b87c9"><path d="M2 21l21-9L2 3v7l15 2-15 2z"/></svg>GET A FREE QUOTE</div>

  <!-- Services -->
  <h2 class="abs sec-title" style="top:733px">OUR <b>SERVICES</b></h2>

  <div class="abs service" style="left:71px;top:810px">
    <div class="service-icon"><svg width="46" height="46" viewBox="0 0 48 48" fill="none" stroke="#0d4f86" stroke-width="2"><circle cx="24" cy="10" r="5"/><path d="M16 24a8 8 0 0 1 16 0"/><path d="M24 26v6M10 32h28M10 32v4M24 32v4M38 32v4"/><circle cx="10" cy="40" r="3"/><circle cx="24" cy="40" r="3"/><circle cx="38" cy="40" r="3"/></svg></div>
    <h3>Nemo Enim Ipsam</h3>
    <p>Sed ut perspiciatis unde omnis iste error sit voluptatem accusantium doloremque laudantium, totam...</p>
  </div>
  <div class="abs service" style="left:335px;top:810px">
    <div class="service-icon"><svg width="46" height="46" viewBox="0 0 48 48" fill="none" stroke="#0d4f86" stroke-width="2"><circle cx="26" cy="20" r="12"/><path d="M14 20h24M26 8c-5 5-5 19 0 24M26 8c5 5 5 19 0 24"/><path d="M6 34c4 0 8 4 14 4h8l-6-4"/></svg></div>
    <h3>Tempora Incidunt</h3>
    <p>Sed ut perspiciatis unde omnis iste error sit voluptatem accusantium doloremque laudantium, totam...</p>
  </div>
  <div class="abs service" style="left:598px;top:810px">
    <div class="service-icon"><svg width="46" height="46" viewBox="0 0 48 48" fill="none" stroke="#0d4f86" stroke-width="2"><path d="M10 26v-4a14 14 0 0 1 28 0v4"/><rect x="7" y="24" width="7" height="11" rx="2"/><rect x="34" y="24" width="7" height="11" rx="2"/><path d="M38 35c0 5-6 7-12 7"/></svg></div>
    <h3>Magni Dolores</h3>
    <p>Sed ut perspiciatis unde omnis iste error sit voluptatem accusantium doloremque laudantium, totam...</p>
  </div>
  <div class="abs service" style="left:861px;top:810px">
    <div class="service-icon"><svg width="46" height="46" viewBox="0 0 48 48" fill="none" stroke="#0d4f86" stroke-width="2"><rect x="10" y="6" width="28" height="10" rx="2"/><rect x="10" y="19" width="28" height="10" rx="2"/><rect x="10" y="32" width="28" height="10" rx="2"/><circle cx="16" cy="11" r="1.5"/><circle cx="16" cy="24" r="1.5"/><circle cx="16" cy="37" r="1.5"/><path d="M24 11h9M24 24h9M24 37h9"/></svg></div>
    <h3>Corporis Suscipit</h3>
    <p>Sed ut perspiciatis unde omnis iste error sit voluptatem accusantium doloremque laudantium, totam...</p>
  </div>

  <!-- Strategy -->
  <section class="abs strategy" role="img" aria-label="Blue-tinted photo of business people in a meeting">
    <h2 class="abs sec-title" style="top:85px">OUR <b>STRATEGY</b></h2>

    <div class="abs strat-item" style="left:100px;top:165px">
      <svg width="46" height="40" viewBox="0 0 48 42" fill="none" stroke="#fff" stroke-width="1.6"><rect x="3" y="6" width="40" height="28"/><path d="M8 28l9-9 7 6 12-13M32 12h4v4M14 34l-4 7M32 34l4 7"/></svg>
      <div><h4>Modi Tempora</h4><div class="rule"></div><p>Nemo enim ipsam voluptatem quia voluptas sit aspernatur aut odit aut fugit, sed quia consequuntur magni dolores eos qui ratione...</p></div>
    </div>
    <div class="abs strat-item" style="left:653px;top:165px">
      <svg width="46" height="44" viewBox="0 0 48 46" fill="none" stroke="#fff" stroke-width="1.6"><rect x="4" y="14" width="16" height="30"/><rect x="20" y="4" width="22" height="40"/><path d="M25 10h4M33 10h4M25 17h4M33 17h4M25 24h4M33 24h4M25 31h4M33 31h4M8 20h8M8 27h8M8 34h8"/></svg>
      <div><h4>Modi Tempora</h4><div class="rule"></div><p>Nemo enim ipsam voluptatem quia voluptas sit aspernatur aut odit aut fugit, sed quia consequuntur magni dolores eos qui ratione...</p></div>
    </div>
    <div class="abs strat-item" style="left:100px;top:310px">
      <svg width="46" height="42" viewBox="0 0 48 44" fill="none" stroke="#fff" stroke-width="1.6"><circle cx="16" cy="12" r="7"/><circle cx="30" cy="16" r="6"/><path d="M3 38a13 13 0 0 1 26 0M24 28a11 11 0 0 1 16 4"/><circle cx="38" cy="36" r="6"/><path d="M38 33v6M35 36h6"/></svg>
      <div><h4>Modi Tempora</h4><div class="rule"></div><p>Nemo enim ipsam voluptatem quia voluptas sit aspernatur aut odit aut fugit, sed quia consequuntur magni dolores eos qui ratione...</p></div>
    </div>
    <div class="abs strat-item" style="left:653px;top:310px">
      <svg width="46" height="44" viewBox="0 0 48 46" fill="none" stroke="#fff" stroke-width="1.6"><circle cx="18" cy="26" r="11"/><circle cx="18" cy="26" r="4"/><path d="M18 12v-3M18 43v-3M4 26h3M29 26h3M8 16l2 2M28 36l-2-2M8 36l2-2M28 16l-2 2"/><circle cx="36" cy="12" r="7"/><circle cx="36" cy="12" r="2.5"/></svg>
      <div><h4>Modi Tempora</h4><div class="rule"></div><p>Nemo enim ipsam voluptatem quia voluptas sit aspernatur aut odit aut fugit, sed quia consequuntur magni dolores eos qui ratione...</p></div>
    </div>
  </section>

  <!-- News -->
  <h2 class="abs sec-title" style="top:1645px">LATEST <b>NEWS</b></h2>

  <div class="abs news-img" style="left:98px;top:1735px;width:299px;height:189px;background:linear-gradient(135deg,#c9b9a3 0%,#8d8c8a 50%,#4a4f55 100%)" role="img" aria-label="Hands typing on a laptop keyboard"></div>
  <h3 class="abs news-title" style="left:455px;top:1758px">Neque porro quisquam est, qui dolorem</h3>
  <p class="abs news-text" style="left:455px;top:1790px">Sed quia non numquam eius modi tempora incidunt ut labore et dolore magnam aliquam quaerat voluptatem. Ut enim ad minimersa veniam, quis nostrum exercitationem ullam voluptate velit esse corporis quam nihil molestiae suscipit...</p>
  <div class="abs btn-outline news-btn" style="left:455px;top:1860px"><svg width="12" height="12" viewBox="0 0 24 24" fill="none" stroke="#1b87c9" stroke-width="2.4"><rect x="3" y="5" width="18" height="16"/><path d="M3 10h18M8 3v4M16 3v4"/></svg>POSTED ON 22 OCT 2016</div>

  <h3 class="abs news-title" style="left:100px;top:1990px">Neque porro quisquam est, qui dolorem</h3>
  <p class="abs news-text" style="left:100px;top:2022px">Sed quia non numquam eius modi tempora incidunt ut labore et dolore magnam aliquam quaerat voluptatem. Ut enim ad minimersa veniam, quis nostrum exercitationem ullam voluptate velit esse corporis quam nihil molestiae suscipit...</p>
  <div class="abs btn-outline news-btn" style="left:100px;top:2092px"><svg width="12" height="12" viewBox="0 0 24 24" fill="none" stroke="#1b87c9" stroke-width="2.4"><rect x="3" y="5" width="18" height="16"/><path d="M3 10h18M8 3v4M16 3v4"/></svg>POSTED ON 22 OCT 2016</div>
  <div class="abs news-img" style="left:802px;top:1965px;width:299px;height:190px;background:linear-gradient(135deg,#5d6266 0%,#9aa0a4 50%,#e8e6e0 100%)" role="img" aria-label="Business team around a table with charts and coffee cups"></div>

  <div class="abs divider"></div>
  <p class="abs quote">Nemo enim ipsam voluptatem quia voluptas sit aspernatur aut odit<br>aut fugit, sed quia ratione voluptatem</p>
  <p class="abs quote-text">Consectetur adipiscing elit, sed do eiusmod tempor incididunt ut labore et dolore magna aliqua. Ut enim ad minim veniam, quis nostrud exercitation ullamco laboris nisi ut aliquip ex ea commodo consequat. Duis aute irure dolor in reprehenderit in voluptate velit esse cillum dolore eu fugiat nulla pariatur. Excepteur sint occaecat cupidatat tempora incidunt ut labore et dolore magnam aliquam quaerat voluptatem. Ut enim ad minima veniam quis nostrum exercitationem ullam corporis...</p>
  <div class="abs btn-outline join-btn"><svg width="11" height="11" viewBox="0 0 24 24" fill="#1b87c9"><circle cx="12" cy="7" r="5"/><path d="M2 23a10 10 0 0 1 20 0z"/></svg>JOIN WITH US</div>

  <!-- Footer -->
  <footer class="abs footer" role="img" aria-label="Blue-tinted photo of a modern glass building">
    <div class="abs" style="left:100px;top:80px;width:300px">
      <h4 class="foot-h">ABOUT US</h4>
      <p class="foot-p" style="margin-top:14px">Voluptatem accusantium doloremque laudantium, totam rem aperiam, eaque ipsa quae ab illo inventore veritatis et quasi ipsum voluptatem quia voluptas sit aspernatur aut odit aut fugit, sed quia consequuntur magni...</p>
      <div class="social" style="margin-top:14px"><span></span><span></span><span></span><span></span></div>
    </div>
    <div class="abs" style="left:478px;top:80px;width:280px">
      <h4 class="foot-h">CONTACT US</h4>
      <div class="contact-row" style="margin-top:16px"><svg width="14" height="18" viewBox="0 0 14 18" fill="#fff"><path d="M7 0a7 7 0 0 1 7 7c0 5-7 11-7 11S0 12 0 7a7 7 0 0 1 7-7zm0 4a3 3 0 1 0 0 6 3 3 0 0 0 0-6z"/></svg><p class="foot-p">Accusantium doloremque laudantium, totam<br>Street Name,City-45453</p></div>
      <div class="contact-row" style="margin-top:12px"><svg width="16" height="16" viewBox="0 0 24 24" fill="#fff"><path d="M5 2h4l2 5-2.5 1.5a11 11 0 0 0 6 6L16 12l5 2v4a2 2 0 0 1-2 2A17 17 0 0 1 3 4a2 2 0 0 1 2-2z"/></svg><p class="foot-p">Phone : (555) 214-3690</p></div>
      <div class="contact-row" style="margin-top:12px"><svg width="16" height="14" viewBox="0 0 24 18" fill="#fff"><path d="M0 0h24v18H0zm2 2v1l10 7 10-7V2L12 9z"/></svg><p class="foot-p">Mail : info@korvenza.com</p></div>
    </div>
    <div class="abs" style="left:810px;top:80px">
      <h4 class="foot-h">SEND ME A QUOTE</h4>
      <div class="field" style="margin-top:14px">Name*</div>
      <div class="field" style="margin-top:10px">E-mail*</div>
      <div class="field field-btn" style="margin-top:10px">REQUEST A QUOTE</div>
    </div>
  </footer>

  <div class="abs bottom-links">HOME<span>|</span>WHO WE ARE<span>|</span>OUR SERVICES<span>|</span>OUR STRATEGY<span>|</span>SECURITY<span>|</span>NEWS<span>|</span>CONTACT US</div>
  <div class="abs copyright">COPYRIGHTS © 2016 . KORVENZA | ALLRIGHTS RESERVED.</div>

</div>
</body>
</html>
```